Floor Inspections and Consulting

We provide inspections and consulting services on various floor coverings, e.g. carpet, hardwood, etc. We also do expert witness work for attorneys due to floor covering failures. We current have a logo, just need it incorporated into a new design. I have examples of cards I have found on the internet that capture my attention and make a statement. I have included our original business card, which in my opinion is terrible, but it does have our logo on it.

```html
<!DOCTYPE html>
<html lang="en">
<head>
<meta charset="utf-8">
<title>Keystone Floor Inspections – Business Card</title>
<link href="https://fonts.googleapis.com/css2?family=Jost:wght@400;500&display=swap" rel="stylesheet">
<style>
  :root {
    --page-bg: #f4e0d4;
    --card-bg: #f5cbb8;
    --accent: #c4582a;
    --band: #d98558;
    --mark: #6b3220;
  }
  * { margin: 0; padding: 0; box-sizing: border-box; }
  html, body { width: 1200px; height: 1200px; overflow: hidden; }
  body { background: var(--page-bg); font-family: "Jost", sans-serif; color: var(--accent); position: relative; }

  .card {
    position: absolute; left: 250px; width: 700px; height: 400px;
    background: var(--card-bg);
  }
  .card--front { top: 129px; }
  .card--back { top: 671px; }

  .side-band {
    position: absolute; top: 0; width: 94px; height: 100%;
    background: linear-gradient(90deg, var(--band), #e39c74, var(--band));
  }
  .side-band--left { left: 0; }
  .side-band--right { right: 0; }

  .brand {
    position: absolute; left: 50%; transform: translateX(-50%);
    display: flex; align-items: center; gap: 14px;
    color: var(--accent); font-weight: 500; text-transform: uppercase;
    letter-spacing: 0.04em; line-height: 1.15; white-space: nowrap;
  }
  .brand__dot { border-radius: 50%; background: var(--mark); flex: none; }

  .card--front .brand { top: 150px; font-size: 28px; }
  .card--front .brand__dot { width: 60px; height: 60px; }
  .card--back .brand { top: 100px; font-size: 16px; gap: 10px; }
  .card--back .brand__dot { width: 36px; height: 36px; }

  .service {
    position: absolute; left: 0; right: 0; text-align: center;
    text-transform: uppercase; font-weight: 400;
  }
  .card--front .service { top: 313px; font-size: 23px; }
  .card--back .service { top: 178px; font-size: 12px; }

  .tagline {
    position: absolute; top: 26px; left: 0; right: 0; text-align: center;
    font-size: 14.5px; text-transform: uppercase; letter-spacing: 0.01em;
  }

  .contact { position: absolute; left: 120px; top: 252px; }
  .contact__name { font-size: 27px; text-transform: uppercase; letter-spacing: 0.01em; margin-bottom: 12px; }
  .contact__line { display: flex; align-items: center; gap: 14px; font-size: 19px; text-transform: uppercase; height: 26px; }
  .contact__icon { width: 16px; height: 16px; flex: none; }
</style>
</head>
<body>
  <section class="card card--front">
    <div class="side-band side-band--left" role="img" aria-label="Checkered border pattern"></div>
    <div class="side-band side-band--right" role="img" aria-label="Checkered border pattern"></div>
    <div class="brand"><span class="brand__dot"></span><span>Keystone Floor<br>Inspections</span></div>
    <p class="service">Analysis &amp; Consulting</p>
  </section>

  <section class="card card--back">
    <div class="side-band side-band--left" role="img" aria-label="Checkered border pattern"></div>
    <div class="side-band side-band--right" role="img" aria-label="Checkered border pattern"></div>
    <p class="tagline">Certified Floor Covering Inspections &amp; Consulting</p>
    <div class="brand"><span class="brand__dot"></span><span>Keystone Floor<br>Inspections</span></div>
    <p class="service">Analysis &amp; Consulting</p>

    <div class="contact">
      <p class="contact__name">Daniel Marsh</p>
      <p class="contact__line">
        <svg class="contact__icon" viewBox="0 0 24 24" aria-hidden="true"><path fill="currentColor" d="M6.6 10.8a15.1 15.1 0 0 0 6.6 6.6l2.2-2.2c.3-.3.7-.4 1-.2 1.1.4 2.3.6 3.6.6.6 0 1 .4 1 1V20c0 .6-.4 1-1 1C10.6 21 3 13.4 3 4c0-.6.4-1 1-1h3.5c.6 0 1 .4 1 1 0 1.3.2 2.5.6 3.6.1.3 0 .7-.2 1z"/></svg>
        303-555-0142
      </p>
      <p class="contact__line">
        <svg class="contact__icon" viewBox="0 0 24 24" aria-hidden="true"><path fill="currentColor" d="M2 5h20v14H2z M4 7v.5l8 5 8-5V7l-8 5z" fill-rule="evenodd"/></svg>
        dan@keystonefloors.com
      </p>
      <p class="contact__line">
        <svg class="contact__icon" viewBox="0 0 24 24" aria-hidden="true"><g fill="none" stroke="currentColor" stroke-width="2"><circle cx="12" cy="12" r="9.5"/><ellipse cx="12" cy="12" rx="4" ry="9.5"/><path d="M2.5 12h19M4 7h16M4 17h16"/></g></svg>
        keystonefloors.com
      </p>
    </div>
  </section>
</body>
</html>
```